IT Business Card Design

My company is a newly started small IT repair business. I operate outside of usual hours except for Saturday.
I am a very experienced and professional Technician.
I would like the business card to express that I am running a professional business and not some home IT business. This should be expressed through the design of the business card.
On the back of the card I would like the name of the company to be displayed.
Updates
Sorry guys, I have updated the requirement to be double sided. Fantastic submissions so far! Keep up the good work.
Hey designers!
Hey Designers!
Thank you all for your hard work!
Target Market(s)
Home to small business users.
Industry/Entity Type
Business
Contact Information for Business Card
Harbourline Computers
Marcus Pembrey (Director)
marcus.pembrey@quenmail.com.au
Operating Hours
5pm-12am Mon - Fri
9am - 5pm Sat
Mobile
0437915263
Requirements
Must have
- The base colour must be matte black. There must be some dark purple. (To go with the "Harbourline" theme)

```html
<!DOCTYPE html>
<html lang="en">
<head>
<meta charset="utf-8">
<title>Harbourline Computers – Business Card</title>
<link rel="stylesheet" href="https://fonts.googleapis.com/css2?family=Arimo:wght@400&display=swap">
<style>
  :root {
    --backdrop: #c8c8c8;
    --card-black: #161616;
    --brand-purple: #a25fc4;
    --ink-white: #f2f2f2;
    --card-shadow: rgba(0, 0, 0, 0.28);
  }
  * { box-sizing: border-box; margin: 0; padding: 0; }
  html, body {
    width: 1200px;
    height: 1000px;
    overflow: hidden;
  }
  body {
    background: var(--backdrop);
    font-family: "Arimo", Helvetica, Arial, sans-serif;
    display: flex;
    flex-direction: column;
    align-items: center;
    justify-content: center;
    gap: 60px;
  }
  .card {
    width: 640px;
    height: 366px;
    background: var(--card-black);
    box-shadow: 0 14px 30px var(--card-shadow);
    display: flex;
    flex-direction: column;
    align-items: center;
    justify-content: center;
    text-align: center;
  }
  /* Front */
  .brand {
    display: flex;
    align-items: center;
    gap: 16px;
  }
  .brand-dot {
    width: 30px;
    height: 30px;
    border-radius: 50%;
    background: var(--brand-purple);
  }
  .brand-name {
    color: var(--brand-purple);
    font-size: 28px;
    font-weight: 400;
    letter-spacing: 2px;
    text-transform: uppercase;
  }
  /* Back */
  .card-back { gap: 0; }
  .back-dot {
    width: 38px;
    height: 38px;
    border-radius: 50%;
    background: var(--brand-purple);
    margin-bottom: 22px;
  }
  .contact-name {
    color: var(--ink-white);
    font-size: 22px;
    letter-spacing: 0.5px;
  }
  .contact-line {
    color: var(--brand-purple);
    font-size: 20px;
    line-height: 1.25;
    letter-spacing: 0.5px;
  }
  .hours-title {
    color: var(--brand-purple);
    font-size: 21px;
    margin-top: 20px;
    letter-spacing: 0.5px;
  }
  .hours-line {
    color: var(--ink-white);
    font-size: 21px;
    line-height: 1.25;
    letter-spacing: 0.5px;
  }
</style>
</head>
<body>
  <section class="card card-front">
    <div class="brand">
      <span class="brand-dot"></span>
      <span class="brand-name">Harbourline Computers</span>
    </div>
  </section>

  <section class="card card-back">
    <span class="back-dot"></span>
    <p class="contact-name">Marcus Pembrey (Director)</p>
    <p class="contact-line">marcus.pembrey@quenmail.com.au</p>
    <p class="contact-line">0437915263</p>
    <p class="hours-title">Operating Hours</p>
    <p class="hours-line">5pm-12am Mon - Fri</p>
    <p class="hours-line">9am - 5pm Sat</p>
  </section>
</body>
</html>
```